Real Estate Team Business Card

We need a business card designed for our real estate team called "Larkspur Realty Group". We would like to receive a final format that would allow us to edit the contact information for new employees as they are added to our team. The difficult part of the design is that we will need to have two logos on the card - both our team name logo for "Larkspur Realty Group" and our company logo for "Corvane Real Estate". Most emphasis should be given to the team logo - maybe double the size of our company logo. (we just have to have the company logo somewhere on the card for legal purposes) The design should somehow illustrate we work in real estate, but still use the beehive/bee concept as a lot of our marketing will involve "bee" sayings. We would also like to use the tagline: "find out what all the buzz is about". We also need to use the "fair housing" logo and "realtor" logos. These can both be small like the company logo.
Target Market(s)
Real Estate
Industry/Entity Type
Real Estate Agent
Contact Information for Business Card
Name: Dylan Marsh Title: Realtor Phone: 801-555-0172 Email: dylan@larkspurrealtrygroup.com Website: www.larkspurrealtygroup.com Facebook: fb/me/larkspurrealtygroup Twitter: @LarkspurRltyGrp
Colors
Designer to choose colors to be used in the design.
Requirements
Must have
- Contact information. Larkspur Realty Group Logo. Corvane Real Estate Logo. Realtor logo. Fair Housing Logo. Tagline: "find out what all the buzz is about".
Nice to have
- It would be nice to illustrate that we work in real estate. It would also be nice to somehow incorporate bees or play off of our beehive logo. We will do a lot of marking using sayings like "let us bee the solution" or "real estate meant to bee" etc.

```html
<!DOCTYPE html>
<html lang="en">
<head>
<meta charset="utf-8">
<title>Larkspur Realty Group – Business Card</title>
<link href="https://fonts.googleapis.com/css2?family=Ubuntu:wght@400;500;700&display=swap" rel="stylesheet">
<style>
  :root {
    --honey: #ffc90b;
    --ink: #130401;
    --paper: #ffffff;
    --board: #e4e4e4;
  }
  * { margin: 0; padding: 0; box-sizing: border-box; }
  html, body { width: 1200px; height: 1200px; overflow: hidden; }
  body {
    position: relative;
    background: var(--board);
    font-family: "Ubuntu", sans-serif;
  }

  /* standalone brand lockup */
  .brand-lockup {
    position: absolute; left: 72px; top: 40px; width: 216px;
    display: flex; flex-direction: column; align-items: center; gap: 18px;
  }
  .brand-lockup .brand-mark { width: 96px; height: 96px; background: var(--honey); }
  .brand-lockup .brand-name {
    font-weight: 700; font-size: 25px; color: var(--ink);
    text-align: center; line-height: 1.15; letter-spacing: 0.04em;
  }

  .card {
    position: absolute; overflow: hidden;
    box-shadow: 0 3px 10px rgba(0,0,0,0.35);
  }

  /* front */
  .card-front { left: 467px; top: 214px; width: 629px; height: 422px; background: var(--paper); }
  .card-front .backdrop { position: absolute; inset: 0; }
  .partner-badges { position: absolute; left: 29px; top: 26px; display: flex; align-items: center; gap: 30px; }
  .company-name { font-weight: 700; font-size: 17px; color: var(--ink); line-height: 1.05; width: 116px; }
  .badge-square { width: 42px; height: 50px; background: var(--ink); }
  .badge-house { width: 56px; height: 58px; background: var(--ink); clip-path: polygon(50% 0, 100% 38%, 100% 100%, 0 100%, 0 38%); }

  .team-brand {
    position: absolute; left: 408px; top: 28px; width: 186px;
    display: flex; flex-direction: column; align-items: center; gap: 14px;
  }
  .team-brand .brand-mark { width: 80px; height: 80px; background: var(--honey); }
  .team-brand .brand-name {
    font-weight: 700; font-size: 20px; color: var(--ink);
    text-align: center; line-height: 1.15; letter-spacing: 0.04em;
  }

  .agent { position: absolute; left: 39px; top: 135px; }
  .agent-name { font-weight: 700; font-size: 28px; color: var(--honey); }
  .agent-title { font-weight: 400; font-size: 27px; color: var(--paper); margin-top: 12px; }

  .contact-list { position: absolute; left: 57px; top: 247px; list-style: none; }
  .contact-list li { display: flex; align-items: center; height: 42px; }
  .contact-list .icon { width: 24px; height: 24px; margin-right: 28px; flex: none; }
  .contact-list span { font-weight: 700; font-size: 18px; color: var(--honey); white-space: nowrap; }
  .contact-list .phone { letter-spacing: 0.32em; }
  .contact-list .email { letter-spacing: 0.01em; }
  .contact-list .facebook { letter-spacing: 0.22em; }
  .contact-list .twitter { letter-spacing: 0.62em; }

  /* back */
  .card-back { left: 467px; top: 688px; width: 651px; height: 436px; background: var(--honey); }
  .card-back .ink-band {
    position: absolute; left: 0; top: 102px; width: 100%; height: 232px;
    background: var(--ink); display: flex; align-items: center; justify-content: center;
  }
  .website { font-weight: 700; font-size: 29px; color: var(--honey); margin-left: 14px; }
</style>
</head>
<body>

  <div class="brand-lockup">
    <div class="brand-mark"></div>
    <div class="brand-name">Larkspur Realty Group</div>
  </div>

  <section class="card card-front">
    <svg class="backdrop" width="629" height="422" viewBox="0 0 629 422">
      <polygon points="0,100 313,104 629,408 629,422 0,422" fill="var(--honey)"/>
      <polygon points="0,118 312,118 610,422 0,422" fill="var(--ink)"/>
    </svg>

    <div class="partner-badges">
      <div class="company-name">Corvane Real Estate</div>
      <div class="badge-square"></div>
      <div class="badge-house"></div>
    </div>

    <div class="team-brand">
      <div class="brand-mark"></div>
      <div class="brand-name">Larkspur Realty Group</div>
    </div>

    <div class="agent">
      <div class="agent-name">Dylan Marsh</div>
      <div class="agent-title">Realtor</div>
    </div>

    <ul class="contact-list">
      <li>
        <svg class="icon" viewBox="0 0 24 24"><circle cx="12" cy="12" r="12" fill="var(--honey)"/><path d="M8 6.5l2 0 1 3-1.5 1.2c.8 1.7 2 2.9 3.8 3.8l1.2-1.5 3 1v2c0 .8-.7 1.4-1.5 1.3C10.5 16.8 7.2 13.5 6.7 8c-.1-.8.5-1.5 1.3-1.5z" fill="var(--ink)"/></svg>
        <span class="phone">801-555-0172</span>
      </li>
      <li>
        <svg class="icon" viewBox="0 0 24 24"><circle cx="12" cy="12" r="12" fill="var(--honey)"/><rect x="6" y="8" width="12" height="8.5" fill="none" stroke="var(--ink)" stroke-width="1.6"/><path d="M6 8l6 5 6-5" fill="none" stroke="var(--ink)" stroke-width="1.6"/></svg>
        <span class="email">dylan@larkspurrealtrygroup.com</span>
      </li>
      <li>
        <svg class="icon" viewBox="0 0 24 24"><circle cx="12" cy="12" r="12" fill="var(--honey)"/></svg>
        <span class="facebook">fb/me/larkspurrealtygroup</span>
      </li>
      <li>
        <svg class="icon" viewBox="0 0 24 24"><circle cx="12" cy="12" r="12" fill="var(--honey)"/></svg>
        <span class="twitter">@LarkspurRltyGrp</span>
      </li>
    </ul>
  </section>

  <section class="card card-back">
    <div class="ink-band">
      <div class="website">www.larkspurrealtygroup.com</div>
    </div>
  </section>

</body>
</html>
```